Online Marketing Agency Website

We are an online marketing agency that specializes in search marketing (SEM) for businesses of all sizes. Our core services include local search marketing, seo, paid search, paid social, graphic design, video production/editing and website design. We have an existing website that we launched a number of years ago but it's very outdated and we're currently too busy to design a new version.

Target Market(s)

Any business that needs online marketing services with an emphasis on search marketing.

Industry/Entity Type

Ad Agency

Number of Pages Required

4 page

Font styles to use
Sans Serif

Requirements
Must have
• Home page, interior page, blog page, contact us page.
Look and feel should be modern and clean and easy to navigate.
Sections for call outs for specific services: Business Marketing Strategy, Content Creation and Marketing, Graphic & Publication Design, Pay Per Click (PPC) Management, Search Engine Optimization, Social Media Management, Video Production & Editing, Website Hosting & Management, Website Design & Development
Use color from logo that was uploaded.

```html
<!DOCTYPE html>
<html lang="en">
<head>
<meta charset="utf-8">
<title>Northpeak Media — Contact</title>
<link rel="stylesheet" href="https://fonts.googleapis.com/css2?family=Exo+2:wght@400;500;600;700&display=swap">
<style>
:root{
  --orange:#ff4a0a;
  --white:#ffffff;
  --ink:#333333;
  --field:#e9e9e9;
  --field-text:#555555;
  --footer:#4a4a4a;
  --footer-field:#6f6f6f;
  --footer-icon:#8a8a8a;
}
*{margin:0;padding:0;box-sizing:border-box}
html,body{width:1200px;height:1163px;overflow:hidden;background:var(--white)}
body{font-family:"Exo 2",sans-serif;color:var(--ink);position:relative}
.abs{position:absolute}

.hero{position:absolute;left:0;top:0;width:1200px;height:444px;overflow:hidden}
.hero-photo{position:absolute;inset:0;background:radial-gradient(ellipse at 55% 45%,#5a4438 0%,#43362f 45%,#3a3330 75%,#4a3e36 100%)}
.hero-curve{position:absolute;left:0;top:0}

.brand{position:absolute;width:108px;text-align:center}
.brand-dot{display:block;width:22px;height:22px;border-radius:50%;background:var(--orange);margin:0 auto 12px}
.brand-name{font-weight:700;font-size:14.5px;color:var(--white);letter-spacing:.2px;white-space:nowrap}

.nav a{position:absolute;top:38px;font-size:11px;color:var(--white);text-decoration:none;text-transform:uppercase;white-space:nowrap}
.nav .caret{display:inline-block;width:6px;height:6px;border-right:1.2px solid var(--white);border-bottom:1.2px solid var(--white);transform:rotate(45deg);margin-left:5px;position:relative;top:-2px}
.btn{position:absolute;background:var(--orange);color:var(--white);border-radius:20px;display:flex;align-items:center;justify-content:center;white-space:nowrap}
.nav .btn-cta{left:843px;top:32px;width:128px;height:28px;font-size:11px;text-transform:uppercase}

.contact-card{position:absolute;left:0;top:0;width:1200px;color:var(--white)}
.contact-title{position:absolute;top:192px;width:1200px;text-align:center;font-weight:700;font-size:21px}
.contact-line{position:absolute;left:552px;font-size:13px;white-space:nowrap}
.contact-icon{position:absolute}
.social-ring{position:absolute;width:36px;height:36px;border-radius:50%;border:1.5px solid var(--orange)}

.ask-title{position:absolute;top:506px;width:1200px;text-align:center;font-size:16px;font-weight:500;letter-spacing:.3px}
.field{position:absolute;left:420px;width:360px;height:28px;border-radius:14px;background:var(--field);font-size:9px;color:var(--field-text);padding:0 15px;display:flex;align-items:center}
.field-area{height:111px;border-radius:12px;align-items:flex-start;padding-top:10px}
.btn-send{left:673px;top:783px;width:107px;height:28px;font-size:9px}

.footer{position:absolute;left:0;top:932px;width:1200px;height:231px;background:var(--footer);color:var(--white)}
.service-list{position:absolute;top:44px;list-style:none;font-size:9px;line-height:18.7px}
.newsletter-title{position:absolute;left:800px;top:38px;font-size:13px}
.newsletter-sub{position:absolute;left:799px;top:70px;font-size:9px}
.footer .field{background:var(--footer-field);color:var(--white);left:799px;width:170px}
.footer .btn-send{left:913px;top:162px;width:57px;height:29px}
.footer-ring{position:absolute;width:28px;height:28px;border-radius:50%;border:1.3px solid var(--footer-icon)}
.copyright{position:absolute;left:419px;top:182px;font-size:9px}
</style>
</head>
<body>

<header class="hero">
  <div class="hero-photo" role="img" aria-label="Warm, softly blurred photograph of two people shaking hands"></div>
  <svg class="hero-curve" width="1200" height="444" viewBox="0 0 1200 444" aria-hidden="true">
    <path d="M449 0 C360 140 210 290 0 281" fill="none" stroke="var(--orange)" stroke-width="2"/>
  </svg>

  <div class="brand" style="left:230px;top:38px">
    <span class="brand-dot"></span>
    <span class="brand-name">NORTHPEAK MEDIA</span>
  </div>

  <nav class="nav">
    <a style="left:450px">Services<span class="caret"></span></a>
    <a style="left:531px">Featured Work</a>
    <a style="left:643px">About</a>
    <a style="left:700px">Blog</a>
    <a style="left:753px">Contact Us</a>
    <span class="btn btn-cta">Free Consultation</span>
  </nav>

  <section class="contact-card">
    <h1 class="contact-title">Northpeak Media</h1>
    <svg class="contact-icon" style="left:520px;top:241px" width="14" height="14" viewBox="0 0 24 24" aria-hidden="true">
      <path fill="#fff" d="M6.6 10.8a15.1 15.1 0 0 0 6.6 6.6l2.2-2.2c.3-.3.7-.4 1-.2 1.1.4 2.3.6 3.6.6.6 0 1 .4 1 1V20c0 .6-.4 1-1 1A17 17 0 0 1 3 4c0-.6.4-1 1-1h3.5c.6 0 1 .4 1 1 0 1.3.2 2.5.6 3.6.1.3 0 .7-.2 1z"/>
    </svg>
    <span class="contact-line" style="top:238px">800-555-0147</span>
    <svg class="contact-icon" style="left:518px;top:268px" width="19" height="13" viewBox="0 0 19 13" aria-hidden="true">
      <rect x="0.5" y="0.5" width="18" height="12" fill="#fff"/>
      <path d="M0.5 0.5 L9.5 7.5 L18.5 0.5 M0.5 12.5 L7 6 M18.5 12.5 L12 6" fill="none" stroke="#4a3d35" stroke-width="1.2"/>
    </svg>
    <span class="contact-line" style="top:265px">hello@northpeakmedia.com</span>
    <span class="social-ring" style="left:515px;top:308px"></span>
    <span class="social-ring" style="left:585px;top:308px"></span>
    <span class="social-ring" style="left:653px;top:308px"></span>
  </section>
</header>

<main>
  <h2 class="ask-title">Ask a question</h2>
  <div class="field" style="top:565px">Name</div>
  <div class="field" style="top:598px">E-mail</div>
  <div class="field" style="top:632px">Phone</div>
  <div class="field field-area" style="top:666px">How can we help you?</div>
  <span class="btn btn-send">Send</span>
</main>

<footer class="footer">
  <div class="brand" style="left:230px;top:34px">
    <span class="brand-dot"></span>
    <span class="brand-name">NORTHPEAK MEDIA</span>
  </div>

  <ul class="service-list" style="left:420px">
    <li>Business Marketing Strategy</li>
    <li>Content Creation and Marketing,</li>
    <li>Graphic &amp; Publication Design</li>
    <li>Pay Per Click (PPC) Management</li>
    <li>Search Engine Optimization</li>
  </ul>
  <ul class="service-list" style="left:602px">
    <li>Social Media Management</li>
    <li>Video Production &amp; Editing</li>
    <li>Website Hosting &amp; Management</li>
    <li>Website Design &amp; Development</li>
  </ul>

  <h3 class="newsletter-title" style="font-weight:400">Stay in touch!</h3>
  <p class="newsletter-sub">Subscrive to our newsletter</p>
  <div class="field" style="top:95px">Name</div>
  <div class="field" style="top:129px">E-mail</div>
  <span class="btn btn-send">Send</span>

  <span class="footer-ring" style="left:229px;top:163px"></span>
  <span class="footer-ring" style="left:270px;top:163px"></span>
  <span class="footer-ring" style="left:311px;top:163px"></span>
  <span class="footer-ring" style="left:352px;top:163px"></span>

  <p class="copyright">© Northpeak Media. 2020. All rights reserved.</p>
</footer>

</body>
</html>
```